Maple Crest Table Business Cards

We need Business cards development for our expanding business. Our Company MapleCrestTable promotes grain free living through products, services and healthy living concepts. Our Products are:
Non-Grain
Non- GMO
Non- Soy
Gluten-Free

Reason: We will need to extend the deadline on our Business Card contest. Thanks, MCT

Industry/Entity Type

Business

```html
<!DOCTYPE html>
<html lang="en">
<head>
<meta charset="utf-8">
<title>Maple Crest Table — Business Card</title>
<link rel="stylesheet" href="https://fonts.googleapis.com/css2?family=Open+Sans:wght@400;600;700&display=swap">
<style>
  :root {
    --card-bg: #ffffff;
    --brand-green: #2f9b1c;
    --deep-green: #1d8a12;
    --fresh-green: #52bd1f;
    --contact-green: #2aa019;
  }
  html, body {
    margin: 0;
    padding: 0;
    width: 1200px;
    height: 686px;
    overflow: hidden;
    background: var(--card-bg);
  }
  .card {
    position: relative;
    width: 1200px;
    height: 686px;
    background: var(--card-bg);
    font-family: "Open Sans", Arial, sans-serif;
  }
  .brand-mark {
    position: absolute;
    left: 150px;
    top: 86px;
    width: 96px;
    height: 96px;
    border-radius: 50%;
    background: var(--brand-green);
  }
  .brand-name {
    position: absolute;
    left: 286px;
    top: 92px;
    margin: 0;
    font-size: 76px;
    font-weight: 700;
    letter-spacing: -1.5px;
    line-height: 1;
    color: var(--brand-green);
  }
  .person {
    position: absolute;
    left: 91px;
    top: 500px;
    display: flex;
    align-items: flex-start;
    gap: 12px;
  }
  .person-icon {
    width: 72px;
    height: 74px;
  }
  .person-name {
    margin: 0;
    font-size: 44px;
    font-weight: 700;
    line-height: 1.05;
    color: var(--deep-green);
  }
  .person-role {
    margin: 0;
    font-size: 27px;
    line-height: 1.1;
    color: var(--fresh-green);
  }
  .contact-list {
    position: absolute;
    left: 764px;
    top: 497px;
    margin: 0;
    padding: 0;
    list-style: none;
  }
  .contact-item {
    display: flex;
    align-items: center;
    height: 34px;
    font-size: 24px;
    color: var(--contact-green);
    white-space: nowrap;
  }
  .contact-icon {
    width: 22px;
    height: 22px;
    margin-right: 20px;
    fill: var(--deep-green);
  }
</style>
</head>
<body>
<main class="card">
  <span class="brand-mark" aria-hidden="true"></span>
  <h1 class="brand-name">MapleCrestTable</h1>

  <section class="person">
    <svg class="person-icon" viewBox="0 0 76 76" aria-hidden="true">
      <path d="M38 6c-11 0-18 8-18 19 0 10 6 21 18 21s18-11 18-21C56 14 49 6 38 6z" fill="none" stroke="#1d8a12" stroke-width="4"/>
      <path d="M28 46c-2 7-10 9-20 13-4 2-5 5-5 11h70c0-6-1-9-5-11-10-4-18-6-20-13" fill="none" stroke="#1d8a12" stroke-width="4" stroke-linejoin="round"/>
    </svg>
    <div class="person-text">
      <h2 class="person-name">John Doe</h2>
      <p class="person-role">Marketing Manager</p>
    </div>
  </section>

  <ul class="contact-list">
    <li class="contact-item">
      <svg class="contact-icon" viewBox="0 0 24 24" aria-hidden="true"><path d="M1 5h22v14H1z"/><path d="M2 6.5l10 7 10-7" fill="none" stroke="#fff" stroke-width="1.6"/></svg>
      www.maplecresttable.com
    </li>
    <li class="contact-item">
      <svg class="contact-icon" viewBox="0 0 24 24" aria-hidden="true"><circle cx="12" cy="12" r="11"/><path d="M6 6c2 1 3 3 2 5s1 3 3 3 1 3 0 5M15 4c-1 2 0 3 2 3s3 2 2 4" fill="none" stroke="#fff" stroke-width="2"/></svg>
      contact@maplecresttable.com
    </li>
    <li class="contact-item">
      <svg class="contact-icon" viewBox="0 0 24 24" aria-hidden="true"><rect x="6" y="1" width="12" height="22" rx="2"/><rect x="8.5" y="4" width="7" height="6" fill="#fff"/><g fill="#fff"><rect x="8.5" y="12" width="2" height="2"/><rect x="11" y="12" width="2" height="2"/><rect x="13.5" y="12" width="2" height="2"/><rect x="8.5" y="15" width="2" height="2"/><rect x="11" y="15" width="2" height="2"/><rect x="13.5" y="15" width="2" height="2"/><rect x="8.5" y="18" width="2" height="2"/><rect x="11" y="18" width="2" height="2"/><rect x="13.5" y="18" width="2" height="2"/></g></svg>
      +(001) 2345 6789
    </li>
    <li class="contact-item">
      <svg class="contact-icon" viewBox="0 0 24 24" aria-hidden="true"><path d="M12 2L1 12h3v10h6v-6h4v6h6V12h3z"/></svg>
      217 Street XYZ,City Name
    </li>
  </ul>
</main>
</body>
</html>
```